Business and Success Coaching Business Card

Need a business card for my coaching business. I coach small businesses, career professionals and, individuals wanting to unlock their human potential and achieve excellence. At the heart of our methodology is the Shaping Purposeful Action Routines Knowingly (SPARK) approach to formulate empowerment, create principles for success and setting achievable outcomes. I would like something that incorporates our new logo, something clean and sharp with a solid darker, but complementary background, color on the card front. The back should be white where there will be room for three questions

Target Market(s)

People looking to advance and improve themselves through a success coach

Industry/Entity Type

Life Coaching

Contact Information for Business Card

Contact information on card.
Business name on front of card
Questions on back

Font styles to use
Other font styles liked:
• Century Gothic or other Serif style fonts that look similar to Century Gothic

Colors

Designer to choose colors to be used in the design.

Requirements
Must have
• Logo on front of card
• Business name - The Steady Forge
• Contact name - Ted Harlow
• Address - Box 4619, Littleton, CO 80127-4619
• Phone number - 303-555-0147
• Email address - harlow.ted@thesteadyforge.example
• Certifications - CLC, CHP, MTC, NLPA
• Back of card
• Three questions on the back of the card:
• If you were at your best, what would you do right now?
• What is the decision you have been avoiding?
• What's one action you could take in the next 10 minutes?
Nice to have
• I would like to see a solid color on the front of the card that compliments the logo.
• Back should be white, or could be contrasting, but need to have the three questions.

```html
<!DOCTYPE html>
<html lang="en">
<head>
<meta charset="utf-8">
<title>The Steady Forge – Business Card</title>
<link href="https://fonts.googleapis.com/css2?family=Montserrat:wght@500;700&family=Lato:wght@400;700&display=swap" rel="stylesheet">
<style>
  :root {
    --bg: #8f8f8f;
    --paper: #f7f8fa;
    --navy: #1b3068;
    --navy-deep: #162a5c;
    --sky: #3f7fcc;
    --sky-soft: #4a88c9;
    --ink: #1d2f63;
    --rule: #9fb3d6;
    --on-dark: #e9eef8;
  }
  * { box-sizing: border-box; margin: 0; padding: 0; }
  html, body { width: 1200px; height: 802px; overflow: hidden; }
  body {
    background: var(--bg);
    font-family: "Lato", sans-serif;
    position: relative;
  }
  .card {
    position: absolute;
    width: 540px;
    height: 309px;
    top: 246px;
    overflow: hidden;
  }
  .card--front { left: 40px; background: var(--paper); }
  .card--back { left: 620px; background: var(--navy); }

  /* front */
  .front-top-stripe { position: absolute; left: 0; top: 0; width: 100%; height: 6px; background: var(--sky); }
  .front-bottom-shape { position: absolute; left: 0; bottom: 0; width: 100%; height: 60px; }
  .brand {
    position: absolute; left: 30px; top: 118px; width: 180px;
    display: flex; align-items: center; gap: 8px;
    color: var(--navy); font-family: "Montserrat", sans-serif; font-weight: 700; font-size: 15px;
  }
  .brand-dot { width: 12px; height: 12px; border-radius: 50%; background: var(--sky); flex: none; }
  .divider { position: absolute; left: 232px; top: 62px; width: 1.5px; height: 176px; background: var(--navy); }
  .contact { position: absolute; left: 258px; top: 58px; width: 270px; color: var(--ink); }
  .contact-name { font-family: "Montserrat", sans-serif; font-size: 23px; font-weight: 700; color: var(--navy); margin-bottom: 10px; }
  .contact-name .surname { font-weight: 500; color: var(--sky); }
  .contact-row { display: flex; align-items: center; gap: 14px; font-size: 11.5px; line-height: 1.3; padding: 4px 0; }
  .contact-icon { width: 14px; height: 14px; flex: none; fill: var(--sky); }
  .contact-text { border-bottom: 1px solid var(--rule); padding-bottom: 4px; min-width: 60px; white-space: nowrap; }
  .contact-row:last-child .contact-text { border-bottom: none; }

  /* back */
  .back-top-shape { position: absolute; left: 0; top: 0; width: 100%; height: 120px; }
  .back-brand {
    position: absolute; left: 0; top: 58px; width: 100%;
    display: flex; justify-content: center; align-items: center; gap: 8px;
    color: var(--on-dark); font-family: "Montserrat", sans-serif; font-weight: 700; font-size: 15px;
  }
  .back-brand .brand-dot { background: var(--on-dark); }
  .band-questions { position: absolute; left: 0; top: 120px; width: 100%; height: 96px; background: var(--navy-deep);
    display: flex; flex-direction: column; justify-content: center; align-items: center; gap: 9px; }
  .question { color: var(--on-dark); font-size: 11px; }
  .band-light { position: absolute; left: 0; top: 216px; width: 100%; height: 56px; background: var(--sky-soft); }
  .band-foot { position: absolute; left: 0; top: 272px; width: 100%; height: 37px; background: var(--navy); }
</style>
</head>
<body>

<section class="card card--front" aria-label="Card front">
  <div class="front-top-stripe"></div>
  <svg class="front-bottom-shape" viewBox="0 0 540 60" preserveAspectRatio="none" aria-hidden="true">
    <path d="M0 36 H190 C205 36 212 52 232 52 H540 V60 H0 Z" fill="var(--navy)"/>
    <path d="M0 36 H190 C205 36 212 52 232 52 H540 V54 H230 C210 54 203 38 188 38 H0 Z" fill="var(--sky)"/>
  </svg>

  <div class="brand"><span class="brand-dot"></span><span>The Steady Forge</span></div>
  <div class="divider"></div>

  <div class="contact">
    <h1 class="contact-name">Ted <span class="surname">Harlow</span></h1>
    <div class="contact-row">
      <svg class="contact-icon" viewBox="0 0 16 16" aria-hidden="true"><path d="M8 1 L15 7.5 H13 V15 H9.5 V10.5 H6.5 V15 H3 V7.5 H1 Z"/></svg>
      <span class="contact-text">Box 4619, Cedar Hollow,<br>ST 00127-4619</span>
    </div>
    <div class="contact-row">
      <svg class="contact-icon" viewBox="0 0 16 16" aria-hidden="true"><path d="M3.5 1 L6 4.5 L4.5 6.5 C5.5 8.5 7.5 10.5 9.5 11.5 L11.5 10 L15 12.5 L13 15 C7 15 1 9 1 3 Z"/></svg>
      <span class="contact-text">303-555-0147</span>
    </div>
    <div class="contact-row">
      <svg class="contact-icon" viewBox="0 0 16 16" aria-hidden="true"><path d="M1 3 H15 V13 H1 Z M2.5 4.5 V11.5 H13.5 V4.5 L8 8.8 Z M3 4 L8 7.8 L13 4 Z" fill-rule="evenodd"/></svg>
      <span class="contact-text">harlow.ted@thesteadyforge.example</span>
    </div>
    <div class="contact-row">
      <svg class="contact-icon" viewBox="0 0 16 16" aria-hidden="true"><circle cx="8" cy="7" r="5.5"/><path d="M5 11 L4 15.5 L8 13.5 L12 15.5 L11 11 Z"/></svg>
      <span class="contact-text">CLC, CHP, MTC, NLPA</span>
    </div>
    <div class="contact-row">
      <svg class="contact-icon" viewBox="0 0 16 16" aria-hidden="true"><path d="M8 1 A7 7 0 1 0 8.01 1 Z M8 2.5 A5.5 5.5 0 1 1 7.99 2.5 Z" fill-rule="evenodd"/><path d="M1.5 7.3 H14.5 V8.7 H1.5 Z M7.3 1.5 H8.7 V14.5 H7.3 Z"/></svg>
      <span class="contact-text">www.thesteadyforge.example</span>
    </div>
  </div>
</section>

<section class="card card--back" aria-label="Card back">
  <svg class="back-top-shape" viewBox="0 0 540 120" preserveAspectRatio="none" aria-hidden="true">
    <rect width="540" height="120" fill="var(--sky-soft)"/>
    <path d="M0 0 H540 V22 H150 C125 22 118 44 95 44 H0 Z" fill="var(--navy)"/>
    <path d="M0 44 H95 C118 44 125 22 150 22 H540 V120 H0 Z" fill="var(--navy)" opacity="0.85"/>
  </svg>
  <div class="back-brand"><span class="brand-dot"></span><span>The Steady Forge</span></div>
  <div class="band-questions">
    <p class="question">If you were at your best, what would you do right now?</p>
    <p class="question">What is the decision you have been avoiding?</p>
    <p class="question">What's one action you could take in the next 10 minutes?</p>
  </div>
  <div class="band-light"></div>
  <div class="band-foot"></div>
</section>

</body>
</html>
```